Clean and modern business cards

Looking for an updated business card design for my dental office “corvanta dental” . Looking for a modern clean / sleek design . I’m thinking black background but open to seeing other options . One side needs to have an appointment card . Card needs to have logo, dentist name , phone, email , address . I’ve attached couple of cards I thought were cool as well as my logo
Target Market(s)
Dental patients
Industry/Entity Type
Dentistry
Contact Information for Business Card
Phone email address

```html
<!DOCTYPE html>
<html lang="en">
<head>
<meta charset="utf-8">
<title>Corvanta Dental – Business Card</title>
<link rel="stylesheet" href="https://fonts.googleapis.com/css2?family=Mulish:wght@400;500;700;800&display=swap">
<style>
  :root {
    --page: #eef0ea;
    --card: #1c1c1c;
    --white: #ffffff;
    --field: #e9e9e9;
    --yellow: #f2c830;
    --lime: #9cc33b;
    --teal: #35a9c5;
    --purple: #7d2fa0;
    --ink: #1c1c1c;
  }
  * { box-sizing: border-box; margin: 0; padding: 0; }
  html, body {
    width: 1200px; height: 1026px; overflow: hidden;
    background: var(--page);
    font-family: "Mulish", sans-serif;
  }
  .card {
    position: absolute; left: 185px;
    width: 830px; height: 474px;
    background: var(--card);
    box-shadow: 0 6px 18px rgba(0,0,0,.18);
    overflow: hidden;
  }
  .card--front { top: 24px; }
  .card--back { top: 528px; }

  .brand-mark {
    position: absolute; border-radius: 50%;
    background: var(--purple);
  }
  .card--front .brand-mark { left: 72px; top: 40px; width: 400px; height: 400px; }

  .front-identity {
    position: absolute; right: 70px; top: 302px; text-align: right;
  }
  .dentist-name {
    color: var(--lime); font-size: 16px; font-weight: 500; letter-spacing: .4px;
    margin-bottom: 6px;
  }
  .brand-name { color: var(--white); font-weight: 800; line-height: 1; }
  .brand-name__main { display: block; font-size: 52px; letter-spacing: .5px; }
  .brand-name__sub { display: block; font-size: 20px; letter-spacing: 7px; margin-top: 8px; margin-right: -7px; }

  .back-brand {
    position: absolute; left: 58px; top: 52px; width: 216px;
    display: flex; flex-direction: column; align-items: center; gap: 16px;
  }
  .back-brand .brand-mark { position: static; width: 150px; height: 150px; }
  .back-brand__name {
    color: var(--white); font-size: 20px; font-weight: 800; letter-spacing: .5px;
  }

  .bubble-accent {
    position: absolute; left: 518px; top: 56px; width: 174px; height: 60px;
    border-radius: 10px;
    background: linear-gradient(90deg, var(--teal), var(--purple));
    opacity: .55;
  }
  .appointment { position: absolute; left: 345px; top: 113px; width: 430px; }
  .appointment__title {
    margin-left: 93px; height: 40px; border-radius: 20px;
    background: var(--yellow); color: var(--ink);
    font-weight: 800; font-size: 17.5px; letter-spacing: .2px;
    display: flex; align-items: center; justify-content: center;
  }
  .appointment__row { display: flex; align-items: center; margin-top: 7px; }
  .appointment__label { width: 93px; font-size: 22px; font-weight: 500; padding-left: 8px; }
  .appointment__label--date { color: var(--lime); }
  .appointment__label--time { color: var(--teal); }
  .appointment__field { flex: 1; height: 40px; border-radius: 20px; background: var(--field); }
  .appointment__note {
    position: absolute; left: 345px; top: 256px; width: 430px;
    text-align: center; color: var(--yellow); font-size: 17.5px; line-height: 24px;
  }

  .contact-list { position: absolute; left: 52px; top: 302px; list-style: none; }
  .contact-list li {
    display: flex; align-items: center; gap: 10px;
    height: 32px; font-size: 15.5px; font-weight: 500;
  }
  .contact-list svg { width: 17px; height: 17px; flex: none; }
  .contact--web { color: var(--yellow); }
  .contact--phone { color: var(--teal); }
  .contact--mail { color: var(--lime); }
  .address {
    position: absolute; left: 53px; top: 404px;
    color: var(--white); font-size: 15.5px; letter-spacing: .3px;
  }
</style>
</head>
<body>

<section class="card card--front" aria-label="Business card front">
  <div class="brand-mark" aria-hidden="true"></div>
  <div class="front-identity">
    <p class="dentist-name">Dr. ELIAS VARONEK</p>
    <h1 class="brand-name">
      <span class="brand-name__main">CORVANTA</span>
      <span class="brand-name__sub">DENTAL</span>
    </h1>
  </div>
</section>

<section class="card card--back" aria-label="Business card back, appointment card">
  <div class="back-brand">
    <div class="brand-mark" aria-hidden="true"></div>
    <p class="back-brand__name">CORVANTA DENTAL</p>
  </div>

  <div class="bubble-accent" role="img" aria-label="Colourful bubble decoration"></div>
  <div class="appointment">
    <div class="appointment__title">YOUR NEXT APPOINTMENT IS:</div>
    <div class="appointment__row">
      <span class="appointment__label appointment__label--date">DATE</span>
      <span class="appointment__field"></span>
    </div>
    <div class="appointment__row">
      <span class="appointment__label appointment__label--time">TIME</span>
      <span class="appointment__field"></span>
    </div>
  </div>
  <p class="appointment__note">To cancel or reschedule please notify us at least<br>48 hours prior to your scheduled appointment.</p>

  <ul class="contact-list">
    <li class="contact--web">
      <svg viewBox="0 0 20 20" aria-hidden="true"><circle cx="10" cy="10" r="10" fill="currentColor"/><circle cx="10" cy="10" r="5.5" fill="none" stroke="#1c1c1c" stroke-width="1.4"/><ellipse cx="10" cy="10" rx="2.3" ry="5.5" fill="none" stroke="#1c1c1c" stroke-width="1.2"/><line x1="4.5" y1="10" x2="15.5" y2="10" stroke="#1c1c1c" stroke-width="1.2"/></svg>
      www.corvantadental.ca
    </li>
    <li class="contact--phone">
      <svg viewBox="0 0 20 20" aria-hidden="true"><circle cx="10" cy="10" r="10" fill="currentColor"/><rect x="7" y="4.5" width="6" height="11" rx="1.3" fill="#1c1c1c"/><rect x="8" y="6" width="4" height="6.5" fill="currentColor"/></svg>
      (204) 555-0182
    </li>
    <li class="contact--mail">
      <svg viewBox="0 0 20 20" aria-hidden="true"><circle cx="10" cy="10" r="10" fill="currentColor"/><rect x="5" y="6.5" width="10" height="7" rx="1" fill="#1c1c1c"/><polyline points="5.5,7 10,10.6 14.5,7" fill="none" stroke="currentColor" stroke-width="1.2"/></svg>
      contact@corvantadental.ca
    </li>
  </ul>
  <p class="address">420 LARCHMONT AVE, WINNIPEG, MB</p>
</section>

</body>
</html>
```